6x11 Postcard for Moving Company

Must have company logo and the company slogan underneath: "The Moving Company You Can Trust And Rely On!". Must have company phone number: 858-271-4489. Must have company email, website and address:
info@haulwise-depot.com
www.haulwise-depot.com
4175 Brisbee Lane, Suite K7,
San Diego, CA 92187
Must have company licenses listed in the following format:
CAL-T# 507384 | CA# 812957 | MC# 364208 | USDOT# 4918203

Must include the following services:
Packing - Moving - Unpacking
Loading - Unloading
Storage In Transit
Long Term Storage
Local - Long Distance
Residential - Commercial
Licensed - Insured
Free Onsite and Video Estimates

And please include the following text above or below the phone number: "Call For FREE Friendly Estimates and Advice!"

Target Market(s)

New Homes that go on sale and Home that were sold and in pending status.

Industry/Entity Type

Moving Company

Colors

Designer to choose colors to be used in the design.

Requirements
Must have
• A photo of a family on the front of the postcard. Must be looking like a real photo of the actual owner of the company with wife and 2 kids (not just a basic stock family photo). Must have Zorbix Shield Logo and the text "Zorbix Shielded". Must say/include 5 star rating on Quibo, Zorbix, Tallisync, Chatterloom, Gildpost. Must include KWR A+ Accreditation Logo. Must include the Certified Truvanta Logo (see attached) and the California Tru Vanta badege. Must have a Book Online Option. Must leave space for NXDL permit for postage. Must include the following deals: $250 Off Long Distance Moves, $50 Off Local Moves, Free Boxes (*call for details), 1 Month Storage Free. (in smaller text must say: *Offers can not be combined with other offers)

```html
<!DOCTYPE html>
<html lang="en">
<head>
<meta charset="utf-8">
<title>HaulWise Depot Postcard</title>
<link rel="stylesheet" href="https://fonts.googleapis.com/css2?family=Oswald:wght@500;700&family=Lato:wght@400;700;900&display=swap">
<style>
:root{
  --red:#e8202a;
  --navy:#2b3a67;
  --ink:#1b1b1f;
  --white:#ffffff;
  --stage:#9a9a9a;
  --line:#e3e3e3;
  --muted:#cfd3de;
}
*{margin:0;padding:0;box-sizing:border-box}
html,body{width:1200px;height:1200px;overflow:hidden;background:var(--stage)}
body{position:relative;font-family:'Lato',sans-serif;color:var(--ink)}
.card{position:absolute;left:122px;width:957px;height:522px;background:var(--white);overflow:hidden}
.card--front{top:63px}
.card--back{top:625px}
.abs{position:absolute}

/* front */
.family-photo{left:0;top:0;width:957px;height:375px;background:linear-gradient(90deg,#f3f3f1 0%,#ece9e4 35%,#cbb79c 55%,#e8e2da 75%,#d9d6d2 100%)}
.brand-front{left:24px;top:168px;font-family:'Oswald',sans-serif;font-weight:700;font-size:31px;color:var(--red);letter-spacing:-.5px;display:flex;align-items:center;gap:8px}
.brand-front .dot{width:18px;height:18px;border-radius:50%;background:var(--red)}
.slogan{left:0;top:240px;width:439px;height:185px;background:var(--red);color:var(--white);padding:18px 0 0 21px;line-height:1}
.slogan .l1{font-family:'Oswald',sans-serif;font-weight:700;font-size:44px;letter-spacing:-.3px}
.slogan .l2,.slogan .l3{font-size:47px;font-weight:400;margin-top:4px;letter-spacing:-.5px}
.slogan b{font-weight:900}
.front-phone{left:470px;top:368px;display:flex;align-items:center;gap:12px;font-family:'Oswald',sans-serif;font-weight:700;font-size:33px;color:var(--ink)}
.front-web{left:720px;top:392px;display:flex;align-items:center;gap:12px;color:var(--white);font-weight:700;font-size:17px}
.badges{left:0;top:425px;width:957px;height:97px;display:flex;align-items:center;justify-content:space-between;padding:0 22px 0 22px}
.badge{display:flex;align-items:center;gap:6px;font-weight:700;color:var(--navy)}
.badge .name{font-size:17px}
.badge .stars{color:#f5a623;font-size:11px;letter-spacing:1px;display:block}
.badge .stack{display:flex;flex-direction:column;line-height:1.05}
.badge .chk{width:32px;height:32px;border-radius:50%;background:#1ea34a}
.badge .sq{width:14px;height:14px;background:var(--red)}
.plain-seal{width:92px;height:34px;border-radius:4px;background:#0f5ea8}
.plain-ring{width:44px;height:44px;border-radius:50%;border:4px solid var(--navy)}

/* back */
.back-brand{left:21px;top:22px;font-family:'Oswald',sans-serif;font-weight:700;font-size:37px;line-height:1.1;color:var(--red);letter-spacing:-.6px;white-space:nowrap}
.back-address{left:328px;top:48px;color:var(--white);font-size:11px;line-height:16px;display:flex;gap:7px;white-space:nowrap}
.services-title{left:0;top:95px;display:flex;align-items:center;gap:12px;font-family:'Oswald',sans-serif;font-weight:500;font-size:22px;color:var(--white)}
.services-title .bar{width:15px;height:32px;background:var(--red)}
.services{color:var(--white);font-size:12.5px;list-style:none}
.services li{height:29px;display:flex;align-items:center;gap:8px;white-space:nowrap}
.tick{width:12px;height:12px;flex:none}
.rule{left:15px;top:284px;width:477px;height:1px;background:var(--muted)}
.offer{left:21px;top:300px;width:256px;height:102px;border:1.5px dashed var(--red)}
.offer-head{position:absolute;left:-1px;top:-1px;width:256px;height:27px;background:var(--red);color:var(--white);text-align:center;font-size:17px;line-height:27px;font-weight:700}
.deal{position:absolute;top:30px;width:128px;text-align:center;color:var(--white)}
.deal .amt{font-family:'Oswald',sans-serif;font-weight:700;font-size:38px;line-height:1.05}
.deal .amt sup{color:var(--red);font-size:20px;vertical-align:top}
.deal .amt small{font-family:'Lato',sans-serif;font-weight:400;font-size:12px}
.deal .what{font-size:12px}
.deal--long{left:0}
.deal--local{left:128px;border-left:1.5px dashed var(--red);height:62px}
.book{left:296px;top:310px;display:flex;align-items:center}
.book .btn-ring{width:42px;height:42px;border-radius:50%;background:var(--red);border:3px solid var(--white);position:relative;z-index:1}
.book .btn-label{background:var(--red);color:var(--white);font-family:'Oswald',sans-serif;font-weight:700;font-size:20px;height:32px;line-height:32px;padding:0 18px 0 18px;margin-left:-8px;border-radius:0 16px 16px 0}
.perks{left:310px;top:366px;color:var(--white);font-size:12.5px;list-style:none}
.perks li{height:22px;display:flex;align-items:center;gap:8px}
.back-phone{left:21px;top:424px}
.back-phone .num{display:flex;align-items:center;gap:8px;font-weight:700;font-size:36px;line-height:1;color:var(--ink);white-space:nowrap}
.back-phone .sub{font-size:12px;margin:5px 0 0 22px;white-space:nowrap}
.back-contact{left:318px;top:437px;color:var(--white);font-size:12px;line-height:24px;white-space:nowrap}
.back-contact div{display:flex;align-items:center;gap:10px}
.licenses{left:18px;top:499px;color:var(--white);font-size:9.5px;white-space:nowrap}
.fine{left:338px;top:493px;color:var(--white);font-size:6.5px;line-height:8px}
.fine-rule{left:316px;top:492px;width:1px;height:20px;background:var(--muted)}
.stamp{left:833px;top:50px;width:72px;height:81px;background:#e9e9e9}
.addr-line{left:554px;width:351px;height:1px;background:var(--line)}
</style>
</head>
<body>

<section class="card card--front">
  <div class="abs family-photo" role="img" aria-label="Photo of the company owner with his wife and two children, smiling among moving boxes in a bright living room"></div>

  <div class="abs brand-front"><span class="dot"></span>HAULWISE DEPOT</div>

  <div class="abs slogan">
    <div class="l1">THE MOVING COMPANY</div>
    <div class="l2">YOU CAN <b>TRUST</b></div>
    <div class="l3">AND <b>RELY ON!</b></div>
  </div>

  <svg class="abs" style="left:0;top:360px" width="957" height="70" viewBox="0 0 957 70">
    <polygon points="437,0 718,0 675,55 437,55" fill="#ffffff"/>
    <polygon points="443,55 676,55 668,65 437,65" fill="#e8202a"/>
    <polygon points="700,25 957,25 957,65 675,65" fill="#2b3a67"/>
  </svg>
  <div class="abs front-phone">
    <svg width="22" height="34" viewBox="0 0 22 34"><path d="M6 2 L10 1 L12 9 L8 11 Q7 17 10 23 L14 22 L17 30 L13 32 Q3 32 2 17 Q2 5 6 2Z" fill="#e8202a"/></svg>
    858-271-4489
  </div>
  <div class="abs front-web">
    <svg width="20" height="20" viewBox="0 0 20 20" fill="none" stroke="#fff" stroke-width="1.6"><circle cx="10" cy="10" r="8.5"/><ellipse cx="10" cy="10" rx="3.8" ry="8.5"/><path d="M1.5 10h17M3 5.5h14M3 14.5h14"/></svg>
    www.haulwise-depot.com
  </div>

  <div class="abs badges">
    <div class="badge"><span class="chk"></span><span class="stack"><span class="name" style="font-size:12px">Zorbix Shielded</span><span class="stars">★★★★★</span></span></div>
    <div class="badge"><span class="stack"><span class="name">Quibo</span><span class="stars" style="color:#e8202a">★★★★★</span></span></div>
    <div class="badge"><span class="stack"><span class="name">Zorbix</span><span class="stars">★★★★★</span></span></div>
    <div class="badge"><span class="sq"></span><span class="stack"><span class="name">Tallisync</span><span class="stars">★★★★★</span></span></div>
    <div class="badge"><span class="stack"><span class="name">Chatterloom</span><span class="stars">★★★★★</span></span></div>
    <div class="badge"><span class="stack"><span class="name">Gildpost</span><span class="stars">★★★★★</span></span></div>
    <div class="plain-seal" role="img" aria-label="Accreditation A+ badge"></div>
    <div class="plain-ring" role="img" aria-label="Certified mover badge"></div>
  </div>
</section>

<section class="card card--back">
  <svg class="abs" style="left:0;top:0" width="500" height="522" viewBox="0 0 500 522">
    <rect x="0" y="0" width="500" height="522" fill="#2b3a67"/>
    <polygon points="0,0 330,0 290,80 0,80" fill="#ffffff"/>
    <polygon points="340,6 500,6 500,20 333,20" fill="#e8202a"/>
    <polygon points="0,420 500,420 500,483 0,483" fill="#e8202a"/>
    <polygon points="0,420 318,420 288,483 0,483" fill="#ffffff"/>
  </svg>

  <div class="abs back-brand">HAULWISE DEPOT</div>
  <div class="abs back-address">
    <svg width="12" height="16" viewBox="0 0 12 16"><path d="M6 15 C2 10 1 8 1 6 A5 5 0 0 1 11 6 C11 8 10 10 6 15Z" fill="none" stroke="#e8202a" stroke-width="1.5"/><circle cx="6" cy="6" r="1.8" fill="#e8202a"/></svg>
    <div>4175 Brisbee Lane, Suite K7,<br>San Diego, CA 92187</div>
  </div>

  <div class="abs services-title"><span class="bar"></span>OUR SERVICES</div>
  <ul class="abs services" style="left:38px;top:130px">
    <li><svg class="tick" viewBox="0 0 12 12"><circle cx="6" cy="6" r="5" fill="none" stroke="#e8202a" stroke-width="1.4"/><path d="M3.5 6l2 2 5-5" fill="none" stroke="#e8202a" stroke-width="1.6"/></svg>Packing - Moving - Unpacking</li>
    <li><svg class="tick" viewBox="0 0 12 12"><circle cx="6" cy="6" r="5" fill="none" stroke="#e8202a" stroke-width="1.4"/><path d="M3.5 6l2 2 5-5" fill="none" stroke="#e8202a" stroke-width="1.6"/></svg>Loading - Unloading</li>
    <li><svg class="tick" viewBox="0 0 12 12"><circle cx="6" cy="6" r="5" fill="none" stroke="#e8202a" stroke-width="1.4"/><path d="M3.5 6l2 2 5-5" fill="none" stroke="#e8202a" stroke-width="1.6"/></svg>Storage In Transit</li>
    <li><svg class="tick" viewBox="0 0 12 12"><circle cx="6" cy="6" r="5" fill="none" stroke="#e8202a" stroke-width="1.4"/><path d="M3.5 6l2 2 5-5" fill="none" stroke="#e8202a" stroke-width="1.6"/></svg>Long Term Storage</li>
    <li><svg class="tick" viewBox="0 0 12 12"><circle cx="6" cy="6" r="5" fill="none" stroke="#e8202a" stroke-width="1.4"/><path d="M3.5 6l2 2 5-5" fill="none" stroke="#e8202a" stroke-width="1.6"/></svg>Local - Long Distance</li>
  </ul>
  <ul class="abs services" style="left:296px;top:130px">
    <li><svg class="tick" viewBox="0 0 12 12"><circle cx="6" cy="6" r="5" fill="none" stroke="#e8202a" stroke-width="1.4"/><path d="M3.5 6l2 2 5-5" fill="none" stroke="#e8202a" stroke-width="1.6"/></svg>Residential - Commercial</li>
    <li><svg class="tick" viewBox="0 0 12 12"><circle cx="6" cy="6" r="5" fill="none" stroke="#e8202a" stroke-width="1.4"/><path d="M3.5 6l2 2 5-5" fill="none" stroke="#e8202a" stroke-width="1.6"/></svg>Licensed - Insured</li>
    <li><svg class="tick" viewBox="0 0 12 12"><circle cx="6" cy="6" r="5" fill="none" stroke="#e8202a" stroke-width="1.4"/><path d="M3.5 6l2 2 5-5" fill="none" stroke="#e8202a" stroke-width="1.6"/></svg>Free Onsite and Video Estimates</li>
    <li><svg class="tick" viewBox="0 0 12 12"><circle cx="6" cy="6" r="5" fill="none" stroke="#e8202a" stroke-width="1.4"/><path d="M3.5 6l2 2 5-5" fill="none" stroke="#e8202a" stroke-width="1.6"/></svg>Daily Intra-State Routes</li>
    <li><svg class="tick" viewBox="0 0 12 12"><circle cx="6" cy="6" r="5" fill="none" stroke="#e8202a" stroke-width="1.4"/><path d="M3.5 6l2 2 5-5" fill="none" stroke="#e8202a" stroke-width="1.6"/></svg>Weekly Inter-State Routes</li>
  </ul>

  <div class="abs rule"></div>

  <div class="abs offer">
    <div class="offer-head">SPECIAL OFFER DISCOUNT</div>
    <div class="deal deal--long"><div class="amt"><sup>$</sup>250 <small>Off</small></div><div class="what">Long Distance Moves</div></div>
    <div class="deal deal--local"><div class="amt"><sup>$</sup>50 <small>Off</small></div><div class="what">Local Moves</div></div>
  </div>

  <div class="abs book">
    <span class="btn-ring"></span>
    <span class="btn-label">BOOK ONLINE</span>
  </div>
  <ul class="abs perks">
    <li><svg class="tick" viewBox="0 0 12 12"><circle cx="6" cy="6" r="5" fill="none" stroke="#e8202a" stroke-width="1.4"/><path d="M3.5 6l2 2 5-5" fill="none" stroke="#e8202a" stroke-width="1.6"/></svg>FREE BOXES*</li>
    <li><svg class="tick" viewBox="0 0 12 12"><circle cx="6" cy="6" r="5" fill="none" stroke="#e8202a" stroke-width="1.4"/><path d="M3.5 6l2 2 5-5" fill="none" stroke="#e8202a" stroke-width="1.6"/></svg>1 MONTH STORAGE FREE*</li>
  </ul>

  <div class="abs back-phone">
    <div class="num">
      <svg width="14" height="28" viewBox="0 0 22 34"><path d="M6 2 L10 1 L12 9 L8 11 Q7 17 10 23 L14 22 L17 30 L13 32 Q3 32 2 17 Q2 5 6 2Z" fill="#e8202a"/></svg>
      858-271-4489
    </div>
    <div class="sub">Call For FREE Friendly Estimates and Advice!</div>
  </div>
  <div class="abs back-contact">
    <div><svg width="18" height="12" viewBox="0 0 18 12" fill="none" stroke="#fff" stroke-width="1.4"><rect x="1" y="1" width="16" height="10"/><path d="M1 1l8 6 8-6"/></svg>info@haulwise-depot.com</div>
    <div><svg width="16" height="16" viewBox="0 0 20 20" fill="none" stroke="#fff" stroke-width="1.6"><circle cx="10" cy="10" r="8.5"/><ellipse cx="10" cy="10" rx="3.8" ry="8.5"/><path d="M1.5 10h17"/></svg>www.haulwise-depot.com</div>
  </div>

  <div class="abs licenses">CAL-T# 507384 | CA# 812957 | MC# 364208 | USDOT# 4918203</div>
  <div class="abs fine-rule"></div>
  <div class="abs fine">*call for details<br>*Offers can not be combined with other offers.</div>

  <div class="abs stamp"></div>
  <div class="abs addr-line" style="top:189px"></div>
  <div class="abs addr-line" style="top:262px"></div>
  <div class="abs addr-line" style="top:334px"></div>
  <div class="abs addr-line" style="top:407px"></div>
</section>

</body>
</html>
```